Building company with a modern and unique product looking for a business card to help us stand out

We currently have a logo but as our business has grown, we feel that our business card is not reflecting our modern and high quality product and help us stand out from the crowd. Our business is mainly in the construction of new homes using a unique method and materials that makes our homes fire proof, vermin and pest resistant and rated to the maximum cyclone category (category 5). We need a business card that helps us stand out as well as communicating professionalism, high quality and trustworthiness. I have attached our current logo with a black and white option, as well as our business card which is double sided. We would like to retain as much of the information that is currently on our business cards, but presented in a more sleek way. We do like our current colour palette ( white, black, yellow and grey) and have been looking primarily at business cards with a black background however we are open to other combinations of colour and layout as long as we stand out. Please feel free to tweak our logo to make it more suitable for a business card, we like the black option that we use but we have had trouble trying to get the white area to match the rest of the logo and blend effectively into a business card. Please do not hesitate to contact us with any questions as we really want this to be successful!

Target Market(s)

Large contracts including government and larger companies

Industry/Entity Type

Business

We will be providing this business card to potential clients including key government ministers and large funding companies, our business card should show that we are professional and reliable.

Requirements
Must have
• It must be easy to read and pleasing to the eye, It must contain as much of the information on the current business card and unless something really stands out, we will most likely pick a design that has all of the information included. It must include our logo of course and have some colour included.
Nice to have
• We are looking for a high end business card and would like to see designs that reflect this. We like the gloss/matte contrast, plastic cards with opaque/coloured areas and unique features not seen on everyday paper business cards. It would be nice to see a few different colour combinations, we are open to new ideas so please feel free to take some artistic licence.
Should not have
• Must not be too busy, difficult to read or be distracting from the information conveyed. Other than this please feel free to add your own touches and make it unique!

```html
<!DOCTYPE html>
<html lang="en">
<head>
<meta charset="utf-8">
<title>Kestrel Building Company – Business Card</title>
<link href="https://fonts.googleapis.com/css2?family=Arvo:wght@400;700&family=Open+Sans:wght@400&display=swap" rel="stylesheet">
<style>
  :root {
    --backdrop: #e7e4df;
    --card: #f5f5f3;
    --ink: #151515;
    --band: #141414;
    --band-warm: #4a3b16;
    --gold: #c9981f;
    --divider: #9a9a9a;
    --text: #1c1c1c;
  }
  * { margin: 0; padding: 0; box-sizing: border-box; }
  html, body {
    width: 1200px; height: 969px; overflow: hidden;
    background: var(--backdrop);
  }
  .card {
    position: absolute; left: 100px; top: 200px;
    width: 1000px; height: 569px;
    background: var(--card);
    border: 1px solid #cfcfcf;
    box-shadow: 0 10px 30px rgba(0,0,0,0.12);
    overflow: hidden;
  }
  .header-art {
    position: absolute; left: 0; top: 0; width: 1000px; height: 200px;
    background: linear-gradient(180deg, var(--band) 0%, var(--band) 45%, var(--band-warm) 100%);
  }
  .brand {
    position: absolute; left: 90px; top: 300px; width: 360px;
    font-family: "Arvo", serif; font-weight: 700; color: var(--ink);
    font-size: 40px; line-height: 1.15; text-align: center;
  }
  .brand-mark {
    display: block; width: 22px; height: 22px; margin: 0 auto 16px;
    background: var(--ink);
  }
  .divider {
    position: absolute; left: 509px; top: 260px;
    width: 1px; height: 245px; background: var(--divider);
  }
  .person { position: absolute; left: 560px; top: 250px; }
  .person-name {
    font-family: "Arvo", serif; font-weight: 700;
    font-size: 36px; letter-spacing: 1px; color: var(--ink);
  }
  .person-title {
    font-family: "Arvo", serif; font-weight: 400;
    font-size: 25px; color: var(--gold); margin-top: 2px;
  }
  .contacts {
    position: absolute; left: 566px; top: 356px; list-style: none;
    font-family: "Open Sans", sans-serif; font-size: 22px; color: var(--text);
  }
  .contacts li { display: flex; align-items: center; height: 38.5px; }
  .contacts svg { width: 20px; height: 20px; margin-right: 12px; fill: var(--ink); flex: none; }
</style>
</head>
<body>
  <div class="card">
    <div class="header-art" role="img" aria-label="Black header band with a gold roofline graphic"></div>

    <div class="brand">
      <span class="brand-mark"></span>
      Kestrel Building<br>Company
    </div>

    <div class="divider"></div>

    <div class="person">
      <div class="person-name">Callum Ridley</div>
      <div class="person-title">Managing Director</div>
    </div>

    <ul class="contacts">
      <li>
        <svg viewBox="0 0 24 24" aria-hidden="true"><path d="M6.6 10.8a15.1 15.1 0 0 0 6.6 6.6l2.2-2.2a1 1 0 0 1 1-.25 11.4 11.4 0 0 0 3.6.57 1 1 0 0 1 1 1V20a1 1 0 0 1-1 1A17 17 0 0 1 3 4a1 1 0 0 1 1-1h3.5a1 1 0 0 1 1 1c0 1.25.2 2.45.57 3.57a1 1 0 0 1-.25 1z"/></svg>
        0491 570 213
      </li>
      <li>
        <svg viewBox="0 0 24 24" aria-hidden="true"><path d="M7 1h10a2 2 0 0 1 2 2v18a2 2 0 0 1-2 2H7a2 2 0 0 1-2-2V3a2 2 0 0 1 2-2zm0 3v14h10V4zm5 15.2a1.2 1.2 0 1 0 0 2.4 1.2 1.2 0 0 0 0-2.4z"/></svg>
        (02) 61 555 480
      </li>
      <li>
        <svg viewBox="0 0 24 24" aria-hidden="true"><path d="M2 5h20v14H2zm2 2v.5l8 5 8-5V7zm0 2.8V17h16V9.8l-8 5z"/></svg>
        office@kestrelbuild.com
      </li>
      <li>
        <svg viewBox="0 0 24 24" aria-hidden="true"><path d="M12 2a10 10 0 1 0 0 20 10 10 0 0 0 0-20zm6.9 6h-3a15.7 15.7 0 0 0-1.4-3.6A8 8 0 0 1 18.9 8zM12 4a14 14 0 0 1 1.9 4h-3.8A14 14 0 0 1 12 4zM4.3 14a8.2 8.2 0 0 1 0-4h3.4a16.5 16.5 0 0 0 0 4zm.8 2h3a15.7 15.7 0 0 0 1.4 3.6A8 8 0 0 1 5.1 16zm3-8h-3a8 8 0 0 1 4.4-3.6A15.7 15.7 0 0 0 8.1 8zM12 20a14 14 0 0 1-1.9-4h3.8A14 14 0 0 1 12 20zm2.3-6H9.7a14.7 14.7 0 0 1 0-4h4.6a14.7 14.7 0 0 1 0 4zm.2 5.6a15.7 15.7 0 0 0 1.4-3.6h3a8 8 0 0 1-4.4 3.6zm1.8-5.6a16.5 16.5 0 0 0 0-4h3.4a8.2 8.2 0 0 1 0 4z"/></svg>
        www.kestrelbuild.com
      </li>
    </ul>
  </div>
</body>
</html>
```